Texas Recycling and dump company needs Flyer design

We need a flyer design for a new company based in Austin Texas called 'Salvage Grove'. We receive dump materials on our property along with sell repurposed materials. We would like our design to include our logo along with add some creative designs to the flyer. Please use the attached image file as an outline. Blank boxes can be used for additional images.

Target Market(s)

Handing out flyers to new companies and hopefully getting contracts with them.

Font styles to use
Serif
Sans Serif

Requirements
Must have
• double sided
• images
Nice to have
• QR code with our website

```html
<!DOCTYPE html>
<html lang="en">
<head>
<meta charset="utf-8">
<title>Salvage Grove Flyer</title>
<link rel="stylesheet" href="https://fonts.googleapis.com/css2?family=Cabin:wght@600;700&family=Questrial&display=swap">
<style>
  :root {
    --page: #e9eaec;
    --paper: #ffffff;
    --green: #8cc63f;
    --blue: #1f6fc1;
    --tile: #d4d4d4;
    --tile-text: #a8a8a8;
    --deal-a: #ef4a1d;
    --deal-b: #f7931e;
    --deal-edge: #fbd24a;
    --leaf-soft: #cfe8a8;
    --asphalt-a: #3a4044;
    --asphalt-b: #2a2f33;
    --soil-a: #5a4433;
    --soil-b: #3a2a20;
  }
  * { margin: 0; padding: 0; box-sizing: border-box; }
  html, body { width: 1200px; height: 916px; overflow: hidden; background: var(--page); }
  .canvas { position: relative; width: 1200px; height: 916px; }
  .flyer { position: absolute; top: 118px; width: 492px; height: 696px; background: var(--paper); overflow: hidden; }
  .flyer--front { left: 86px; }
  .flyer--back { left: 622px; }
  .box { position: absolute; }
  .photo-asphalt { background: linear-gradient(135deg, var(--asphalt-a), var(--asphalt-b)); }
  .photo-soil { background: linear-gradient(135deg, var(--soil-a), var(--soil-b)); }
  .tile { background: var(--tile); display: flex; align-items: center; justify-content: center; text-align: center;
    font-family: "Cabin", sans-serif; font-weight: 600; font-size: 26px; line-height: 1.25; color: var(--tile-text); letter-spacing: 1px; }
  .leaf { background: var(--leaf-soft); border-radius: 50%; }
  .sprout { background: linear-gradient(180deg, rgba(140,198,63,0) 0%, rgba(140,198,63,.35) 100%); border-radius: 40px 40px 0 0; }

  /* front */
  .brand { position: absolute; left: 0; right: 0; top: 104px; text-align: center;
    font-family: "Questrial", sans-serif; font-size: 29px; color: var(--blue); letter-spacing: 1px; }
  .brand-mark { display: inline-block; width: 14px; height: 14px; background: var(--green); margin-right: 8px; vertical-align: 3px; }
  .headline { position: absolute; left: 0; right: 0; top: 526px; text-align: center;
    font-family: "Cabin", sans-serif; font-weight: 700; font-size: 28px; line-height: 35px; color: var(--blue); letter-spacing: .5px; }
  .address { position: absolute; left: 0; right: 0; top: 612px; text-align: center;
    font-family: "Questrial", sans-serif; font-size: 15.5px; color: var(--blue); letter-spacing: .3px; }
  .footer-band { position: absolute; left: 0; right: 0; top: 650px; height: 46px; background: var(--green);
    display: flex; align-items: center; justify-content: space-between; padding: 0 21px 0 26px;
    font-family: "Cabin", sans-serif; font-weight: 600; font-size: 15px; color: #fff; letter-spacing: .3px; }

  /* back */
  .header-band { position: absolute; left: 0; right: 0; top: 0; height: 104px; background: var(--green); }
  .title { position: absolute; left: 0; right: 0; top: 24px; text-align: center;
    font-family: "Cabin", sans-serif; font-weight: 700; font-size: 33px; color: #fff; letter-spacing: 1.5px; }
  .deal-badge { position: absolute; left: 126px; top: 86px; width: 210px; height: 38px;
    background: linear-gradient(90deg, var(--deal-a), var(--deal-b)); border: 2px solid var(--deal-edge); border-radius: 4px;
    font-family: "Cabin", sans-serif; font-weight: 700; font-size: 26px; line-height: 34px; color: #fff; padding-left: 10px; }
  .flame { position: absolute; left: 326px; top: 76px; width: 32px; height: 44px; border-radius: 50% 50% 40% 40%;
    background: radial-gradient(circle at 50% 70%, #ffe07a, #f7931e 70%); }
  .base-band { position: absolute; left: 0; right: 0; top: 680px; height: 16px; background: var(--green); }
</style>
</head>
<body>
<div class="canvas">

  <section class="flyer flyer--front">
    <div class="brand"><span class="brand-mark"></span>SALVAGE GROVE</div>

    <div class="box" role="img" aria-label="Photo of grey concrete texture" style="left:87px;top:166px;width:163px;height:139px;border-radius:24px 0 0 0;background:linear-gradient(135deg,#d9d9d9,#a8a8a8);"></div>
    <div class="box photo-asphalt" role="img" aria-label="Photo of an asphalt road" style="left:261px;top:183px;width:144px;height:122px;border-radius:0 24px 0 0;"></div>
    <div class="box" role="img" aria-label="Photo of a shovel lifting rich soil" style="left:106px;top:316px;width:144px;height:176px;border-radius:0 0 0 32px;background:linear-gradient(160deg,#566a3a,#3a2a1e 55%,#6b3a1f);"></div>
    <div class="box" role="img" aria-label="Photo of a pile of broken wood scraps" style="left:261px;top:316px;width:119px;height:102px;border-radius:0 0 24px 0;background:linear-gradient(135deg,#8c8578,#5a554c);"></div>
    <div class="box tile" style="left:261px;top:426px;width:87px;height:74px;border-radius:0 0 18px 0;">C&amp;D</div>

    <div class="box leaf" role="img" aria-label="Small green leaf" style="left:410px;top:202px;width:12px;height:18px;"></div>
    <div class="box leaf" role="img" aria-label="Small green leaf" style="left:78px;top:320px;width:12px;height:18px;"></div>
    <div class="box leaf" role="img" aria-label="Small green leaf" style="left:352px;top:424px;width:18px;height:24px;"></div>
    <div class="box sprout" role="img" aria-label="Green sprout seedlings" style="left:9px;top:558px;width:75px;height:92px;"></div>

    <div class="headline">CLEANER THE PRODUCT<br>LOWER THE PRICE</div>
    <div class="address">2810 CEDAR HOLLOW RD AUSTIN</div>
    <div class="footer-band"><span>512-555-0148</span><span>WWW.SALVAGEGROVE.COM</span></div>
  </section>

  <section class="flyer flyer--back">
    <div class="header-band"></div>
    <div class="title">LANDSCAPE MATERIALS</div>
    <div class="deal-badge">&amp; HOT DEALS</div>
    <div class="flame" role="img" aria-label="Flame graphic"></div>

    <div class="box" role="img" aria-label="Photo of dry autumn leaves mulch" style="left:40px;top:168px;width:154px;height:132px;border-radius:22px 0 0 0;background:linear-gradient(135deg,#8a6a4a,#4a3526 60%,#a88660);"></div>
    <div class="box tile" style="left:204px;top:192px;width:128px;height:108px;border-radius:0 22px 0 0;">HOT<br>DEALS?</div>
    <div class="box photo-soil" role="img" aria-label="Photo of tilled topsoil" style="left:340px;top:204px;width:112px;height:96px;border-radius:0 0 20px 0;"></div>

    <div class="box tile" style="left:58px;top:310px;width:136px;height:116px;border-radius:0 0 0 24px;">DEC<br>GRA</div>
    <div class="box tile" style="left:204px;top:310px;width:128px;height:96px;border-radius:0 0 20px 0;"></div>
    <div class="box tile" style="left:340px;top:310px;width:112px;height:110px;border-radius:0 0 20px 20px;">BASE</div>

    <div class="box" role="img" aria-label="Photo of blue-grey river gravel" style="left:90px;top:434px;width:104px;height:90px;border-radius:20px 0 0 0;background:linear-gradient(135deg,#9aa3ad,#6c7782);"></div>
    <div class="box tile" style="left:204px;top:414px;width:128px;height:110px;border-radius:20px 0 0 0;"></div>
    <div class="box photo-asphalt" role="img" aria-label="Photo of an asphalt road" style="left:340px;top:428px;width:112px;height:96px;border-radius:0 20px 0 0;"></div>

    <div class="box tile" style="left:82px;top:532px;width:112px;height:96px;border-radius:20px 0 0 0;"></div>
    <div class="box tile" style="left:204px;top:532px;width:112px;height:96px;border-radius:0 0 20px 0;"></div>
    <div class="box tile" style="left:326px;top:532px;width:126px;height:108px;border-radius:0 20px 0 0;"></div>

    <div class="box leaf" role="img" aria-label="Small green leaf" style="left:330px;top:164px;width:16px;height:26px;"></div>
    <div class="box leaf" role="img" aria-label="Small green leaf" style="left:34px;top:310px;width:14px;height:20px;"></div>
    <div class="box leaf" role="img" aria-label="Small green leaf" style="left:454px;top:414px;width:12px;height:18px;"></div>
    <div class="box leaf" role="img" aria-label="Small green leaf" style="left:72px;top:494px;width:14px;height:20px;"></div>
    <div class="box sprout" role="img" aria-label="Green sprout seedlings" style="left:26px;top:611px;width:60px;height:69px;"></div>

    <div class="base-band"></div>
  </section>

</div>
</body>
</html>
```